Business Card Design for Quorvane

Need a business card designed for Quorvane employees.
- 2 sided business card
- Front:
Company Logo (file attached)
Background could be:white with perhaps a red/black stripe on the left
OR
Background could be: OR dark red-black gradient: be creative
Include the following on the front:
Martin Delacroy
Founder & CEO
martin.delacroy@quorvane-example.com
+1 555.013.4782
quorvane-example.com
- Back: White color background with company logo
Text under the logo: Invoice Automation 2.0
** be creative about the font, mix of upper and lower case and colors for the text **
Target Market(s)
We are a software company marketing our products to large and medium sized businesses.
Industry/Entity Type
Business

```html
<!DOCTYPE html>
<html lang="en">
<head>
<meta charset="utf-8">
<title>Quorvane Business Card</title>
<link rel="stylesheet" href="https://fonts.googleapis.com/css2?family=Quicksand:wght@400;500;600&display=swap">
<style>
  :root {
    --backdrop: #ece6d2;
    --card: #ffffff;
    --ink-dark: #2a0d0d;
    --ink-grey: #3a3a3a;
    --brand-red: #a3080c;
    --brand-red-deep: #5e0406;
    --accent-red: #c0272d;
    --stripe-black: #0d0d0d;
    --mark-grey: #bdbdbd;
  }
  * { box-sizing: border-box; margin: 0; padding: 0; }
  html, body { width: 1200px; height: 560px; overflow: hidden; }
  body {
    background: var(--backdrop);
    font-family: "Quicksand", sans-serif;
    position: relative;
  }
  .card {
    position: absolute;
    top: 132px;
    width: 520px;
    height: 297px;
    background: var(--card);
    box-shadow: 0 6px 18px rgba(90, 70, 30, 0.18);
    overflow: hidden;
  }
  .card--back { left: 50px; }
  .card--front { left: 630px; }

  /* Back side */
  .back-logo {
    position: absolute;
    left: 0; right: 0; top: 92px;
    display: flex;
    align-items: center;
    justify-content: center;
    gap: 18px;
  }
  .back-logo .mark {
    width: 70px; height: 70px; border-radius: 50%;
    background: var(--mark-grey);
  }
  .back-logo .wordmark {
    font-size: 56px; font-weight: 500; letter-spacing: 2px;
    color: var(--ink-grey);
  }
  .back-tagline {
    position: absolute;
    left: 178px; right: 40px; top: 178px;
    border-top: 1px solid var(--accent-red);
    padding-top: 6px;
    text-align: right;
    font-size: 15px; font-weight: 500; letter-spacing: 2px;
    color: var(--accent-red);
  }

  /* Front side */
  .stripe-red {
    position: absolute; left: 0; top: 0; bottom: 0; width: 78px;
    background: linear-gradient(180deg, var(--brand-red) 0%, var(--brand-red-deep) 100%);
  }
  .stripe-black {
    position: absolute; left: 78px; top: 0; bottom: 0; width: 8px;
    background: var(--stripe-black);
  }
  .front-logo {
    position: absolute; left: 112px; top: 30px;
    display: flex; align-items: center; gap: 14px;
  }
  .front-logo .mark {
    width: 78px; height: 78px; border-radius: 50%;
    background: var(--mark-grey);
  }
  .front-logo .wordmark {
    font-size: 40px; font-weight: 500; letter-spacing: 1px;
    color: var(--ink-grey);
    line-height: 1;
  }
  .front-logo .tagline {
    font-size: 13px; font-weight: 500;
    color: var(--accent-red);
    text-align: right;
    margin-top: 4px;
  }
  .person {
    position: absolute; left: 120px; top: 152px;
  }
  .person .name {
    font-size: 22px; font-weight: 500; color: var(--ink-dark); line-height: 1.1;
  }
  .person .role {
    font-size: 12px; color: var(--accent-red); margin-top: 1px;
  }
  .contact {
    position: absolute; left: 126px; top: 210px;
    list-style: none;
    font-size: 14px; font-weight: 600; line-height: 1.25;
    color: var(--brand-red-deep);
  }
</style>
</head>
<body>
  <section class="card card--back" aria-label="Card back">
    <div class="back-logo">
      <span class="mark"></span>
      <span class="wordmark">QUORVANE</span>
    </div>
    <p class="back-tagline">INVOICE AUTOMATION 2.0</p>
  </section>

  <section class="card card--front" aria-label="Card front">
    <div class="stripe-red"></div>
    <div class="stripe-black"></div>
    <div class="front-logo">
      <span class="mark"></span>
      <div>
        <div class="wordmark">QUORVANE</div>
        <div class="tagline">Invoice Automation 2.0</div>
      </div>
    </div>
    <div class="person">
      <p class="name">MARTIN DELACROY</p>
      <p class="role">Founder &amp; CEO</p>
    </div>
    <ul class="contact">
      <li>martin.delacroy@quorvane-example.com</li>
      <li>+1 555.013.4782</li>
      <li>quorvane-example.com</li>
    </ul>
  </section>
</body>
</html>
```